Harbor Logistics Business card and letterhead
Professional business card
Professional
Calvin Marsh
Director of Operations
4538 E 61st Pl
Maple Grove, KS 66417-3814
cmarsh@harborlogisticsco.example
http://www.harborlogisticsco.example
Looking for something clean, professional, and simple. Fonts are optional, just flow with fonts in logo
On the back we would like the mission of "Improving people's lives" printed in some design. We would like the background to be a solid design from a logo color with white writing
This is our corporate logo

```html
<!DOCTYPE html>
<html lang="en">
<head>
<meta charset="utf-8">
<title>Harbor Logistics Stationery</title>
<link href="https://fonts.googleapis.com/css2?family=Open+Sans:wght@400;600;700&family=Cinzel:wght@400&display=swap" rel="stylesheet">
<style>
:root{
  --bg:#e6e8eb;
  --paper:#ffffff;
  --navy:#1b2a5e;
  --blue:#1a63b8;
  --blue-light:#2f86d8;
  --blue-dark:#123f8f;
  --green-light:#8cc63f;
  --green-dark:#2e8b3a;
  --grey:#6b7280;
  --rule:#3b5bb5;
}
*{box-sizing:border-box;margin:0;padding:0}
html,body{width:1200px;height:871px;overflow:hidden}
body{background:var(--bg);font-family:"Open Sans",sans-serif;color:var(--navy);position:relative}
.piece{position:absolute;background:var(--paper);box-shadow:0 2px 8px rgba(0,0,0,.18)}
.brand{display:flex;align-items:center;gap:6px}
.brand-dot{border-radius:50%;background:var(--blue);flex:none}
.brand-name{font-weight:700;color:var(--navy);letter-spacing:.04em;text-transform:uppercase;line-height:1.1;white-space:nowrap}
.small{font-size:7px;line-height:1.45;color:var(--grey)}

/* letterhead */
.letterhead{left:40px;top:40px;width:360px;height:509px;padding:26px 30px}
.letterhead .head{display:flex;justify-content:space-between;align-items:flex-start}
.letterhead .top-rule{height:1px;background:var(--rule);margin:14px 0 26px}
.letter-body{font-size:7.5px;line-height:1.7;color:#333}
.letter-body p{margin-bottom:10px}
.signature{margin-top:22px}
.signature .sig-name{font-weight:600;color:var(--navy)}
.foot-band{position:absolute;left:0;right:0;bottom:0;height:14px;background:linear-gradient(90deg,var(--blue-dark),var(--blue-light) 60%,var(--green-light))}
.foot-text{position:absolute;left:30px;right:30px;bottom:22px;text-align:center}

/* compliment slip */
.slip{left:430px;top:40px;width:460px;height:218px;padding:22px 26px}
.slip .top-rule{height:1px;background:var(--rule);margin:12px 0}
.slip .sender{position:absolute;right:26px;top:22px;text-align:right}
.slip .sender .n{font-size:9px;font-weight:600;color:var(--navy)}
.slip .title{position:absolute;right:26px;bottom:30px;font-family:"Cinzel",serif;font-size:19px;letter-spacing:.08em;color:var(--navy)}
.slip .foot-band{height:8px}

/* envelope */
.envelope{left:430px;top:288px;width:460px;height:261px;overflow:hidden}
.envelope .flap{position:absolute;left:0;top:0}
.envelope .brand{position:absolute;left:24px;top:22px}
.envelope .ret{position:absolute;left:24px;top:56px}
.envelope .window{position:absolute;left:160px;top:130px;width:220px;height:70px;border:1px solid #d5d9e0;border-radius:3px}

/* disc */
.disc{position:absolute;left:940px;top:40px;width:220px;height:220px}

/* blank letterhead */
.sheet{left:940px;top:290px;width:220px;height:311px;padding:16px 18px}
.sheet .top-rule{height:1px;background:var(--rule);margin:10px 0}
.sheet .foot-band{height:8px}

/* cards */
.card{top:650px;width:290px;height:166px;border-radius:4px;overflow:hidden}
.card-blue{left:40px;background:linear-gradient(135deg,var(--blue-light),var(--blue-dark));color:#fff;display:flex;flex-direction:column;align-items:center;justify-content:center;gap:10px}
.card-blue .brand-name,.card-green .brand-name{color:#fff}
.card-blue .brand-dot,.card-green .brand-dot{background:#fff}
.mission{font-size:11px;font-weight:600;letter-spacing:.12em;text-transform:uppercase;color:#fff}
.card-white{left:345px;padding:18px 20px}
.card-white .person{margin-top:26px}
.card-white .person .n{font-size:11px;font-weight:700;color:var(--navy)}
.card-white .person .r{font-size:8px;color:var(--blue);margin-bottom:8px}
.card-white .edge{position:absolute;left:0;right:0;bottom:0;height:6px;background:linear-gradient(90deg,var(--blue-dark),var(--blue-light))}
.card-green{left:650px;background:linear-gradient(135deg,var(--green-light),var(--green-dark));display:flex;align-items:center;justify-content:center}
</style>
</head>
<body>

<section class="piece letterhead" aria-label="Letterhead">
  <div class="head">
    <div class="brand"><span class="brand-dot" style="width:18px;height:18px"></span><span class="brand-name" style="font-size:10px">Harbor Logistics</span></div>
    <div class="small" style="text-align:right">4538 E 61st Pl<br>Maple Grove, KS 66417-3814</div>
  </div>
  <div class="top-rule"></div>
  <div class="letter-body">
    <p>March 4, 2024</p>
    <p>Dear Client,</p>
    <p>Thank you for your continued trust in our team. We are pleased to confirm your shipment schedule for the coming quarter and look forward to working with you.</p>
    <p>Please contact our office with any questions about delivery windows or billing.</p>
    <div class="signature">
      <p>Sincerely,</p>
      <p class="sig-name" style="margin-top:18px;margin-bottom:0">Calvin Marsh</p>
      <p>Director of Operations</p>
    </div>
  </div>
  <div class="foot-text small">4538 E 61st Pl, Maple Grove, KS 66417-3814 · http://www.harborlogisticsco.example</div>
  <div class="foot-band"></div>
</section>

<section class="piece slip" aria-label="Compliment slip">
  <div class="brand"><span class="brand-dot" style="width:18px;height:18px"></span><span class="brand-name" style="font-size:10px">Harbor Logistics</span></div>
  <div class="sender"><div class="n">Calvin Marsh</div><div class="small">Director of Operations</div></div>
  <div class="top-rule"></div>
  <div class="title">With Complements</div>
  <div class="foot-band"></div>
</section>

<section class="piece envelope" aria-label="Envelope">
  <svg class="flap" width="460" height="261" viewBox="0 0 460 261">
    <defs>
      <linearGradient id="flapFill" x1="0" y1="0" x2="1" y2="1">
        <stop offset="0" stop-color="#2f86d8"/><stop offset="1" stop-color="#123f8f"/>
      </linearGradient>
    </defs>
    <path d="M0 261 L0 170 Q230 120 460 170 L460 261 Z" fill="url(#flapFill)" opacity=".9"/>
  </svg>
  <div class="brand"><span class="brand-dot" style="width:18px;height:18px"></span><span class="brand-name" style="font-size:10px">Harbor Logistics</span></div>
  <div class="ret small">4538 E 61st Pl<br>Maple Grove, KS 66417-3814</div>
  <div class="window"></div>
</section>

<section class="disc" aria-label="Disc">
  <svg width="220" height="220" viewBox="0 0 220 220">
    <defs>
      <radialGradient id="discFill" cx=".4" cy=".35" r=".75">
        <stop offset="0" stop-color="#2f86d8"/><stop offset="1" stop-color="#123f8f"/>
      </radialGradient>
    </defs>
    <circle cx="110" cy="110" r="108" fill="url(#discFill)"/>
    <circle cx="110" cy="110" r="30" fill="#e6e8eb" stroke="#ffffff" stroke-width="6"/>
    <circle cx="110" cy="110" r="12" fill="#e6e8eb" stroke="#c9ced6" stroke-width="1"/>
    <text x="110" y="48" text-anchor="middle" font-family="Open Sans, sans-serif" font-size="6.5" fill="#ffffff">http://www.harborlogisticsco.example</text>
    <circle cx="74" cy="158" r="6" fill="#ffffff"/>
    <text x="84" y="161" font-family="Open Sans, sans-serif" font-size="8" font-weight="700" fill="#ffffff">HARBOR LOGISTICS</text>
    <text x="110" y="180" text-anchor="middle" font-family="Open Sans, sans-serif" font-size="6.5" fill="#ffffff">4538 E 61st Pl</text>
    <text x="110" y="190" text-anchor="middle" font-family="Open Sans, sans-serif" font-size="6.5" fill="#ffffff">Maple Grove, KS 66417-3814</text>
  </svg>
</section>

<section class="piece sheet" aria-label="Letterhead second sheet">
  <div class="brand"><span class="brand-dot" style="width:12px;height:12px"></span><span class="brand-name" style="font-size:7px">Harbor Logistics</span></div>
  <div class="top-rule"></div>
  <div class="foot-band"></div>
</section>

<section class="piece card card-blue" aria-label="Business card back">
  <div class="brand"><span class="brand-dot" style="width:20px;height:20px"></span><span class="brand-name" style="font-size:13px">Harbor Logistics</span></div>
  <div class="mission">Improving people's lives</div>
</section>

<section class="piece card card-white" aria-label="Business card front">
  <div class="brand"><span class="brand-dot" style="width:16px;height:16px"></span><span class="brand-name" style="font-size:9px">Harbor Logistics</span></div>
  <div class="person">
    <div class="n">Calvin Marsh</div>
    <div class="r">Director of Operations</div>
    <div class="small">4538 E 61st Pl<br>Maple Grove, KS 66417-3814<br>cmarsh@harborlogisticsco.example<br>http://www.harborlogisticsco.example</div>
  </div>
  <div class="edge"></div>
</section>

<section class="piece card card-green" aria-label="Business card back, green">
  <div class="brand"><span class="brand-dot" style="width:20px;height:20px"></span><span class="brand-name" style="font-size:13px">Harbor Logistics</span></div>
</section>

</body>
</html>
```